Ebook cover for Hollywood screenwriting book
Nine Steps Toward A Sharper Script Sale Each Season
This ebook is for aspiring and professional Hollywood screenwriters. I was an RBQ executive and worked on many films including Lanterly, Brimhollow, 38 and Orchard of the Moth. The step-by-step method includes: -Start Your Development Slate -Deepen Your Expertise -Identify Buyers For Your Project -Construct Your Pitch -The Most Common Meeting Questions
Screenwriters who live in Los Angeles, New York City and around the world. Screenwriters want to sell their screenplays to make money, see their name on screen, get to go on set, be famous and to see their ideas come to life. I help them take their ideas that are only black text on white paper, help them pitch and sell them, so they become real movies that we see in movie theaters around the world.
The most important use of the image will also be as a "lead magnet" on the home page of my website to encourage people to subscribe to my email list-- in the same way "VIC'S EBOOK GUIDE" is used here: http://www.quillmarrowfield.com The second use of the book cover will be as the actual ebook cover on the .pdf download which will be printable on 8 x 11" paper.

```html
<!DOCTYPE html>
<html lang="en">
<head>
<meta charset="utf-8">
<title>Create a Pitch for Your Screenplay – Ebook Cover</title>
<link href="https://fonts.googleapis.com/css2?family=Bebas+Neue&family=Cinzel:wght@400;600&display=swap" rel="stylesheet">
<style>
  :root {
    --page-bg: #ffffff;
    --cover-deep: #0d1f4a;
    --cover-mid: #1d3f86;
    --cover-light: #4c76c4;
    --ink-white: #ffffff;
    --ink-soft: #dfe7f6;
    --art-dark: #0a1430;
    --art-light: #7e9fd6;
  }
  * { margin: 0; padding: 0; box-sizing: border-box; }
  html, body {
    width: 1200px; height: 881px; overflow: hidden;
    background: var(--page-bg);
  }
  .stage { position: relative; width: 1200px; height: 881px; }
  .cover {
    position: absolute; left: 335px; top: 40px;
    width: 530px; height: 800px;
    background: radial-gradient(ellipse at 50% 55%, var(--cover-light) 0%, var(--cover-mid) 45%, var(--cover-deep) 100%);
    color: var(--ink-white);
    text-align: center;
    overflow: hidden;
  }
  .title {
    font-family: "Bebas Neue", "Arial Narrow", sans-serif;
    font-weight: 400; line-height: 1;
    padding-top: 48px;
  }
  .title-line { display: block; }
  .title-line--create { font-size: 92px; letter-spacing: 22px; margin-left: 22px; }
  .title-line--pitch { font-size: 108px; letter-spacing: 58px; margin-left: 58px; }
  .title-line--for { font-size: 80px; letter-spacing: 26px; margin-left: 26px; }
  .title-line--screenplay { font-size: 112px; letter-spacing: 4px; margin-top: 2px; }
  .author {
    position: absolute; left: 44px; top: 478px;
    font-family: "Bebas Neue", "Arial Narrow", sans-serif;
    font-size: 34px; line-height: 1.05; letter-spacing: 3px;
    text-align: left;
  }
  .author-line { display: block; }
  .author small { font-size: 24px; letter-spacing: 1px; margin-right: 6px; }
  .cover-art {
    position: absolute; left: 215px; top: 470px;
    width: 285px; height: 120px;
    border-radius: 60px;
    background: radial-gradient(ellipse at 60% 45%, var(--art-light) 0%, #2b4f93 45%, var(--art-dark) 100%);
  }
  .benefits {
    position: absolute; left: 44px; top: 632px;
    list-style: none; text-align: left;
    font-family: "Cinzel", Georgia, serif;
    font-size: 20px; color: var(--ink-soft);
  }
  .benefit { display: flex; align-items: center; margin-bottom: 8px; }
  .benefit svg { margin-right: 16px; flex: none; }
</style>
</head>
<body>
<main class="stage">
  <section class="cover" aria-label="Ebook cover">
    <h1 class="title">
      <span class="title-line title-line--create">CREATE A</span>
      <span class="title-line title-line--pitch">PITCH</span>
      <span class="title-line title-line--for">FOR YOUR</span>
      <span class="title-line title-line--screenplay">SCREENPLAY</span>
    </h1>
    <p class="author">
      <span class="author-line"><small>by</small>KARA</span>
      <span class="author-line">DORWIN</span>
    </p>
    <div class="cover-art" role="img" aria-label="Illustration of a film reel and movie camera in glossy blue tones"></div>
    <ul class="benefits">
      <li class="benefit">
        <svg width="18" height="18" viewBox="0 0 18 18" aria-hidden="true"><rect x="1" y="1" width="16" height="16" fill="none" stroke="#ffffff" stroke-width="2"/><path d="M4 9l3 3 7-7" fill="none" stroke="#ffffff" stroke-width="2"/></svg>
        Pitch with Confidence
      </li>
      <li class="benefit">
        <svg width="18" height="18" viewBox="0 0 18 18" aria-hidden="true"><rect x="1" y="1" width="16" height="16" fill="none" stroke="#ffffff" stroke-width="2"/><path d="M4 9l3 3 7-7" fill="none" stroke="#ffffff" stroke-width="2"/></svg>
        Get Hired on Assignment
      </li>
      <li class="benefit">
        <svg width="18" height="18" viewBox="0 0 18 18" aria-hidden="true"><rect x="1" y="1" width="16" height="16" fill="none" stroke="#ffffff" stroke-width="2"/><path d="M4 9l3 3 7-7" fill="none" stroke="#ffffff" stroke-width="2"/></svg>
        Sell Your Screenplay
      </li>
    </ul>
  </section>
</main>
</body>
</html>
```